Business Card Design

We Need a business card design for my company based in Tv Radio and music Productions and hunt Talent.

Industry/Entity Type

Business

Contact Information for Business Card

BrentaVue Production's, Teodor Vignoles,Cell Phone 318 4957310
Musician, Productor, Hunt Talent. Miami Fla. www.brentavue.net Mail. teodorvignoles@mailvana.com

```html
<!DOCTYPE html>
<html lang="en">
<head>
<meta charset="utf-8">
<title>BrentaVue Production's – Business Card</title>
<link href="https://fonts.googleapis.com/css2?family=Open+Sans:wght@400;600;700&display=swap" rel="stylesheet">
<style>
  :root {
    --stage: #e9e6e1;
    --gold-light: #f7dc5a;
    --gold: #e9bd1c;
    --gold-deep: #c9980a;
    --band: #f2c417;
    --wine: #a3211f;
    --ink: #1d1d1d;
    --paper: #ffffff;
    --mist: #e4e6ea;
  }
  * { box-sizing: border-box; margin: 0; padding: 0; }
  html, body { width: 1200px; height: 750px; overflow: hidden; }
  body {
    background: var(--stage);
    font-family: "Open Sans", Arial, sans-serif;
    position: relative;
  }
  .card {
    position: absolute;
    top: 221px;
    width: 540px;
    height: 308px;
    overflow: hidden;
    box-shadow: 0 6px 18px rgba(0,0,0,.18);
  }
  /* ---------- front ---------- */
  .card-front {
    left: 40px;
    background: linear-gradient(135deg, var(--gold-light) 0%, var(--gold) 55%, var(--gold-deep) 100%);
  }
  .front-swirl {
    position: absolute; inset: 0;
    background:
      radial-gradient(ellipse 70% 45% at 20% 25%, rgba(255,255,255,.35), transparent 70%),
      radial-gradient(ellipse 90% 40% at 60% 95%, rgba(255,240,170,.45), transparent 70%);
  }
  .front-art {
    position: absolute;
    left: 200px; top: 28px;
    width: 310px; height: 190px;
    border-radius: 8px;
    background: radial-gradient(ellipse at 60% 45%, #f6d43a 0%, #d9a915 45%, #3a3326 100%);
  }
  .front-name {
    position: absolute;
    left: 200px; top: 232px;
    width: 310px;
    text-align: center;
    font-weight: 700; font-size: 24px; color: var(--wine);
    line-height: 1.2;
  }
  /* ---------- back ---------- */
  .card-back {
    left: 620px;
    background: var(--paper);
  }
  .back-sheen {
    position: absolute; inset: 0;
    background:
      radial-gradient(ellipse 80% 55% at 85% 25%, var(--mist), transparent 70%),
      radial-gradient(ellipse 60% 35% at 70% 70%, #f0f1f4, transparent 70%);
  }
  .holder-name {
    position: absolute; right: 30px; top: 18px;
    font-size: 14px; font-weight: 600; color: var(--wine);
    letter-spacing: .5px; text-transform: uppercase;
  }
  .back-art {
    position: absolute; left: 28px; top: 48px;
    width: 170px; height: 100px;
    border-radius: 6px;
    background: radial-gradient(ellipse at 60% 45%, #f6d43a 0%, #d9a915 45%, #3a3326 100%);
  }
  .back-name {
    position: absolute; left: 212px; top: 84px;
    font-weight: 700; font-size: 20px; color: var(--wine);
    line-height: 1.2;
  }
  .contact-list {
    position: absolute; left: 30px; top: 162px;
    list-style: none;
    display: flex; flex-direction: column; gap: 3px;
  }
  .contact-list li {
    display: flex; align-items: center; gap: 7px;
    font-size: 17px; color: var(--ink);
  }
  .contact-list svg { width: 18px; height: 18px; flex: none; }
  .role-band {
    position: absolute; left: 0; right: 0; bottom: 14px;
    height: 38px;
    background: var(--band);
    border-top: 2px solid var(--paper);
    display: flex; justify-content: space-around; align-items: center;
    font-weight: 700; font-size: 15px; color: var(--wine);
    letter-spacing: 5px;
  }
</style>
</head>
<body>

<section class="card card-front" aria-label="Card front">
  <div class="front-swirl" role="img" aria-label="Soft golden light swirls and sparkles"></div>
  <div class="front-art" role="img" aria-label="Illustration of a vintage microphone in front of a gold star"></div>
  <p class="front-name">BrentaVue's Show</p>
</section>

<section class="card card-back" aria-label="Card back">
  <div class="back-sheen" role="img" aria-label="Faint silver curved light streaks"></div>
  <p class="holder-name">Teodor Vignoles</p>

  <div class="back-art" role="img" aria-label="Illustration of a vintage microphone in front of a gold star"></div>
  <p class="back-name">BrentaVue's Show</p>

  <ul class="contact-list">
    <li>
      <svg viewBox="0 0 24 24" aria-hidden="true"><path fill="#c0392b" d="M6.6 10.8a15 15 0 0 0 6.6 6.6l2.2-2.2a1 1 0 0 1 1-.25 11.4 11.4 0 0 0 3.6.57 1 1 0 0 1 1 1V20a1 1 0 0 1-1 1A17 17 0 0 1 3 4a1 1 0 0 1 1-1h3.5a1 1 0 0 1 1 1c0 1.25.2 2.45.57 3.57a1 1 0 0 1-.25 1z"/></svg>
      318 4957310
    </li>
    <li>
      <svg viewBox="0 0 24 24" aria-hidden="true"><g fill="none" stroke="#c0392b" stroke-width="2"><circle cx="12" cy="12" r="9"/><ellipse cx="12" cy="12" rx="4" ry="9"/><path d="M3 12h18M5 7h14M5 17h14"/></g></svg>
      www.brentavue.net
    </li>
    <li>
      <svg viewBox="0 0 24 24" aria-hidden="true"><rect x="2" y="5" width="20" height="14" rx="2" fill="#c0392b"/><path d="M3 6l9 7 9-7" fill="none" stroke="#fff" stroke-width="1.8"/></svg>
      teodorvignoles@mailvana.com
    </li>
  </ul>

  <div class="role-band">
    <span>Musician</span>
    <span>Productor</span>
    <span>Hunt Talent</span>
  </div>
</section>

</body>
</html>
```